Ductless Mini Split Business Website

Tall Fern Services is looking to design an eye catching educational website about installing Ductless mini splits.

Similar to this company.
https://www.kelvarocomfort.com/

```html
<!DOCTYPE html>
<html lang="en">
<head>
<meta charset="utf-8">
<title>Tall Fern Services – Ductless Experts</title>
<link rel="stylesheet" href="https://fonts.googleapis.com/css2?family=Poppins:wght@400;500;600;700&family=Russo+One&display=swap">
<style>
:root{
  --yellow:#e8b90b;
  --yellow-soft:#f1c61c;
  --dark:#1c1c1c;
  --ink:#222;
  --muted:#555;
  --grey-bg:#f4f4f4;
  --line:#ddd;
  --white:#fff;
}
*{box-sizing:border-box;margin:0;padding:0}
html,body{width:1200px;height:4030px;overflow:hidden}
body{position:relative;background:var(--white);font-family:"Poppins",sans-serif;color:var(--ink)}
.abs{position:absolute}
.heading{font-family:"Russo One",sans-serif;color:var(--dark);text-align:center;position:absolute;left:0;width:1200px}
.sub{font-size:13px;color:var(--muted);text-align:center;position:absolute;left:0;width:1200px}
.btn{position:absolute;display:flex;align-items:center;justify-content:center;gap:12px;border-radius:22px;font-size:14px;font-weight:500}
.btn .dot{width:16px;height:16px;border-radius:50%;background:var(--dark);display:inline-flex;align-items:center;justify-content:center}
.btn-yellow{background:var(--yellow);color:var(--dark)}
.btn-dark{background:var(--dark);color:var(--white)}
.btn-dark .dot{background:var(--yellow)}
.photo{position:absolute}
/* header */
.logo{position:absolute;left:76px;top:26px;display:flex;align-items:center;gap:10px}
.logo .mark{width:34px;height:34px;border-radius:50%;background:var(--yellow)}
.logo .name{font-weight:700;font-size:22px;color:var(--dark);line-height:1}
.logo-tag{position:absolute;left:80px;top:80px;font-weight:700;font-size:16px;color:var(--dark)}
.nav{position:absolute;top:72px;left:500px;display:flex;gap:38px;font-size:14px;color:var(--dark)}
.nav .active{color:var(--yellow)}
.call{position:absolute;left:790px;top:19px;display:flex;gap:10px;align-items:center}
.call .ico{width:30px;height:30px;border-radius:50%;background:var(--yellow);display:flex;align-items:center;justify-content:center}
.call small{display:block;color:var(--yellow);font-size:11px;line-height:1.2}
.call span{font-size:12px}
/* hero */
.hero-title1{left:172px;top:220px;font-family:"Russo One",sans-serif;font-size:26px;color:var(--dark)}
.hero-title2{left:172px;top:250px;font-family:"Russo One",sans-serif;font-size:46px;color:var(--dark)}
.arrow{position:absolute;width:28px;height:28px;border-radius:50%;background:#e4e4e4;display:flex;align-items:center;justify-content:center;font-size:13px;color:#444}
.dots{position:absolute;display:flex;gap:7px}
.dots i{width:6px;height:6px;border-radius:50%;background:#bbb;display:block}
.dots i.on{background:var(--yellow)}
/* about */
.about-text{left:620px;top:776px;width:472px;font-size:12px;line-height:1.3;color:var(--muted)}
.about-text p{margin-bottom:18px}
/* cards */
.service{position:absolute;width:308px;height:266px}
.service .label{position:absolute;left:0;bottom:0;width:100%;height:55px;background:var(--yellow);display:flex;align-items:center;justify-content:center;font-weight:600;font-size:16px;color:var(--dark)}
.blog{position:absolute;width:307px;height:349px;background:var(--white);box-shadow:0 1px 6px rgba(0,0,0,.12)}
.blog h4{position:absolute;left:15px;top:235px;font-size:14px;font-weight:500}
.blog p{position:absolute;left:15px;top:262px;width:280px;font-size:11.5px;line-height:1.3;color:var(--muted)}
.blog a{position:absolute;left:15px;top:320px;font-size:12px;color:var(--muted);text-decoration:underline}
.badge{position:absolute;left:128px;top:152px;width:52px;height:56px}
.badge span{position:absolute;inset:0;display:flex;flex-direction:column;align-items:center;justify-content:center;font-size:12px;font-weight:600;line-height:1.1;color:var(--dark)}
.testi{position:absolute;width:473px;height:230px;border:1px solid var(--line);background:var(--white)}
.testi h5{position:absolute;left:158px;top:50px;font-size:18px;font-weight:500}
.testi .role{position:absolute;left:158px;top:76px;font-size:13px;color:var(--muted)}
.testi p{position:absolute;left:163px;top:100px;width:280px;font-size:12px;line-height:1.3;color:var(--muted)}
.stars{position:absolute;left:163px;top:150px;color:var(--yellow);font-size:12px;letter-spacing:3px}
/* contact */
.field{position:absolute;background:var(--white);font-size:12px;color:#777;padding:10px 14px}
/* footer */
.footer{position:absolute;left:0;top:3688px;width:1200px;height:286px;background:var(--dark);color:var(--white)}
.foot-h{position:absolute;top:106px;font-size:17px}
.foot-list{position:absolute;top:146px;font-size:13px;line-height:17.5px}
.social{position:absolute;left:882px;top:141px;display:flex;gap:8px}
.social i{display:block;width:28px;height:28px;border-radius:50%;background:var(--white)}
.social i:first-child{background:var(--yellow)}
.bottom{position:absolute;top:3990px;font-size:12px;color:var(--ink)}
</style>
</head>
<body>

<!-- Header -->
<header>
  <div class="logo"><span class="mark"></span><span class="name">Tall Fern Services</span></div>
  <div class="logo-tag">DUCTLESS EXPERTS</div>
  <div class="call">
    <span class="ico"><svg width="14" height="14" viewBox="0 0 24 24"><path fill="#1c1c1c" d="M6.6 10.8a15 15 0 006.6 6.6l2.2-2.2a1 1 0 011-.3 11 11 0 003.6.6 1 1 0 011 1V20a1 1 0 01-1 1A17 17 0 013 4a1 1 0 011-1h3.5a1 1 0 011 1 11 11 0 00.6 3.6 1 1 0 01-.3 1z"/></svg></span>
    <div><small>Call Us Now</small><span>+00 123 456 7890</span></div>
  </div>
  <div class="btn btn-yellow" style="left:957px;top:17px;width:166px;height:32px;font-size:13px;">➤ Request a Quote</div>
  <nav class="nav">
    <span class="active">Home</span><span>About us</span><span>Our Services</span><span>Gallery</span><span>Blogs</span><span>FAQ</span><span>Contact us</span>
    <svg width="15" height="15" viewBox="0 0 24 24"><circle cx="10" cy="10" r="7" fill="none" stroke="#1c1c1c" stroke-width="2.5"/><path d="M15 15l6 6" stroke="#1c1c1c" stroke-width="2.5"/></svg>
  </nav>
</header>

<!-- Hero -->
<section>
  <div class="photo" role="img" aria-label="Family relaxing on a sofa beneath a wall-mounted ductless unit" style="left:0;top:120px;width:1200px;height:470px;background:linear-gradient(90deg,#ececec 0%,#e3e3e3 45%,#d2cdc6 70%,#e8e8e8 100%);"></div>
  <div class="abs hero-title1">Make Yourself</div>
  <div class="abs hero-title2">Comfortable</div>
  <div class="btn btn-dark" style="left:172px;top:319px;width:144px;height:32px;font-size:13px;">Read More <span class="dot"><svg width="8" height="8" viewBox="0 0 10 10"><path d="M3 1l4 4-4 4" stroke="#1c1c1c" stroke-width="2" fill="none"/></svg></span></div>
  <div class="arrow" style="left:30px;top:280px;">‹</div>
  <div class="arrow" style="left:1141px;top:280px;">›</div>
  <div class="dots" style="left:580px;top:556px;"><i class="on"></i><i></i><i></i><i></i></div>
</section>

<!-- About -->
<section>
  <svg class="abs" style="left:146px;top:668px;" width="444" height="388" viewBox="0 0 444 388" role="img" aria-label="Technician servicing an outdoor heat pump unit">
    <polygon points="111,0 333,0 444,194 333,388 111,388 0,194" fill="#e6e6e6"/>
    <polygon points="118,12 326,12 430,194 326,376 118,376 14,194" fill="#b9b0a0"/>
  </svg>
  <div class="abs" style="left:562px;top:704px;width:56px;height:56px;border-radius:50%;background:var(--yellow);"></div>
  <div class="abs" style="left:634px;top:716px;font-family:'Russo One',sans-serif;font-size:34px;color:var(--dark);">About us</div>
  <div class="abs about-text">
    <p>Lorem Ipsum is simply dummy text of the printing and typesetting industry has been the industry's standard dummy text ever since the 1500s,</p>
    <p>when an unknown printer took a galley of type and scrambled it to make a type specimen book. It has survived not only five centuries, but also the leap into electronic typesetting, remaining essentially unchanged. It was popularised in the 1960s</p>
    <p>with the release of Letraset sheets containing Lorem Ipsum passages, and more recently with desktop publishing software like Aldus Page Maker next including versions of Lorem Ipsum.</p>
  </div>
  <div class="btn btn-yellow" style="left:621px;top:971px;width:166px;height:37px;">Read More <span class="dot"><svg width="8" height="8" viewBox="0 0 10 10"><path d="M3 1l4 4-4 4" stroke="#fff" stroke-width="2" fill="none"/></svg></span></div>
</section>

<!-- Services -->
<section>
  <svg class="abs" style="left:0;top:1135px;" width="1200" height="530" viewBox="0 0 1200 530" preserveAspectRatio="none">
    <rect x="0" y="15" width="1200" height="515" fill="#f4f4f4"/>
    <polygon points="0,4 300,10 0,26" fill="#e8b90b"/>
    <polygon points="1200,508 880,518 1200,531" fill="#1c1c1c"/>
  </svg>
  <div class="heading" style="top:1180px;font-size:32px;">Our Services</div>
  <div class="sub" style="top:1218px;">How Can We Help You?</div>
  <div class="service" style="left:113px;top:1261px;"><div class="photo" role="img" aria-label="Technician installing an indoor ductless unit" style="inset:0 0 55px 0;background:linear-gradient(135deg,#e9e9e9,#c9c4bb);"></div><div class="label">Ductless Installation</div></div>
  <div class="service" style="left:447px;top:1261px;"><div class="photo" role="img" aria-label="Close-up of a baseboard heater" style="inset:0 0 55px 0;background:linear-gradient(135deg,#d8d8d8,#a9a9a9);"></div><div class="label">Baseboard Heat Replacement</div></div>
  <div class="service" style="left:780px;top:1261px;"><div class="photo" role="img" aria-label="Technician repairing a ductless unit" style="inset:0 0 55px 0;background:linear-gradient(135deg,#f0f0f0,#b9b3a9);"></div><div class="label">Ductless Repairs</div></div>
  <div class="arrow" style="left:60px;top:1377px;">‹</div>
  <div class="arrow" style="left:1110px;top:1370px;background:var(--dark);color:#fff;width:32px;height:32px;">›</div>
  <div class="abs" style="left:477px;top:1553px;width:66px;height:60px;border-radius:50%;background:var(--yellow);"></div>
  <div class="btn btn-yellow" style="left:530px;top:1569px;width:158px;height:36px;">View More</div>
</section>

<!-- Gallery -->
<section>
  <div class="heading" style="top:1704px;font-size:32px;">Gallery</div>
  <div class="photo" role="img" aria-label="Dining room with a wall-mounted ductless unit" style="left:77px;top:1763px;width:336px;height:232px;background:linear-gradient(135deg,#ddd6cc,#8f7a63);"></div>
  <div class="photo" role="img" aria-label="Woman relaxing under a ductless unit in a brick room" style="left:432px;top:1765px;width:336px;height:230px;background:linear-gradient(135deg,#e6e3df,#9c9a97);"></div>
  <div class="photo" role="img" aria-label="Living room with a sofa and a ductless unit" style="left:787px;top:1765px;width:336px;height:230px;background:linear-gradient(135deg,#ebeae8,#c6bfb3);"></div>
  <div class="photo" role="img" aria-label="Ceiling cassette air unit" style="left:77px;top:2012px;width:336px;height:232px;background:linear-gradient(135deg,#f2f2f2,#cfcfcf);"></div>
  <div class="photo" role="img" aria-label="Outdoor condenser units" style="left:432px;top:2014px;width:336px;height:230px;background:linear-gradient(135deg,#555,#2b2b2b);">
    <div class="abs" style="left:17px;top:126px;color:#fff;font-size:13px;">Project Title</div>
    <div class="abs" style="left:17px;top:146px;width:36px;height:2px;background:#fff;"></div>
    <div class="abs" style="left:17px;top:154px;width:300px;color:#fff;font-size:12px;line-height:1.3;">Lorem Ipsum is simply dummy text type set int the world industry.</div>
    <div class="abs" style="left:17px;top:197px;width:16px;height:16px;border-radius:50%;background:var(--yellow);"></div>
  </div>
  <div class="photo" role="img" aria-label="Outdoor heat pump with remote control in hand" style="left:787px;top:2014px;width:336px;height:230px;background:linear-gradient(135deg,#dcdcdc,#7f8f6a);"></div>
  <div class="abs" style="left:474px;top:2254px;width:66px;height:60px;border-radius:50%;background:var(--yellow);"></div>
  <div class="btn btn-yellow" style="left:527px;top:2269px;width:157px;height:37px;">View More <span class="dot"><svg width="8" height="8" viewBox="0 0 10 10"><path d="M3 1l4 4-4 4" stroke="#fff" stroke-width="2" fill="none"/></svg></span></div>
</section>

<!-- Blogs -->
<section>
  <svg class="abs" style="left:0;top:2348px;" width="1200" height="580" viewBox="0 0 1200 580" preserveAspectRatio="none">
    <rect x="0" y="12" width="1200" height="568" fill="#f4f4f4"/>
    <polygon points="0,6 290,12 0,30" fill="#e8b90b"/>
    <polygon points="1200,555 880,566 1200,580" fill="#1c1c1c"/>
  </svg>
  <div class="heading" style="top:2394px;font-size:32px;">Blogs</div>

  <div class="blog" style="left:113px;top:2461px;">
    <div class="photo" role="img" aria-label="Outdoor condenser units beside a house" style="left:0;top:0;width:307px;height:192px;background:linear-gradient(135deg,#c8c4bc,#7d8a66);"></div>
    <svg class="badge" viewBox="0 0 52 56"><polygon points="26,0 52,14 52,42 26,56 0,42 0,14" fill="#e8b90b"/></svg><div class="badge"><span>24<br>DEC</span></div>
    <h4>What is Lorem Ipsum?</h4>
    <p>Lorem Ipsum is simply dummy text the printing and typesetting industry Lorem Ipsum has been dummy text ever since the 1500s,</p>
    <a>Continue..</a>
  </div>
  <div class="blog" style="left:447px;top:2461px;">
    <div class="photo" role="img" aria-label="Rooftop outdoor units in front of buildings" style="left:0;top:0;width:307px;height:192px;background:linear-gradient(135deg,#eef0f2,#9aa7b4);"></div>
    <svg class="badge" viewBox="0 0 52 56"><polygon points="26,0 52,14 52,42 26,56 0,42 0,14" fill="#e8b90b"/></svg><div class="badge"><span>24<br>DEC</span></div>
    <h4>What is Lorem Ipsum?</h4>
    <p>Lorem Ipsum is simply dummy text the printing and typesetting industry Lorem Ipsum has been dummy text ever since the 1500s,</p>
    <a>Continue..</a>
  </div>
  <div class="blog" style="left:781px;top:2461px;">
    <div class="photo" role="img" aria-label="Outdoor condenser unit among garden plants" style="left:0;top:0;width:307px;height:192px;background:linear-gradient(135deg,#dfe2e4,#5f7a4c);"></div>
    <svg class="badge" viewBox="0 0 52 56"><polygon points="26,0 52,14 52,42 26,56 0,42 0,14" fill="#e8b90b"/></svg><div class="badge"><span>24<br>DEC</span></div>
    <h4>What is Lorem Ipsum?</h4>
    <p>Lorem Ipsum is simply dummy text the printing and typesetting industry Lorem Ipsum has been dummy text ever since the 1500s,</p>
    <a>Continue..</a>
  </div>
  <div class="btn btn-yellow" style="left:516px;top:2840px;width:169px;height:36px;">View More <span class="dot"><svg width="8" height="8" viewBox="0 0 10 10"><path d="M3 1l4 4-4 4" stroke="#fff" stroke-width="2" fill="none"/></svg></span></div>
</section>

<!-- Testimonials -->
<section>
  <div class="heading" style="top:2976px;font-size:32px;">Testimonials</div>
  <div class="sub" style="top:3024px;font-size:11px;">What Clients say about us</div>
  <div class="testi" style="left:113px;top:3066px;">
    <svg class="abs" style="left:22px;top:50px;" width="118" height="128" viewBox="0 0 118 128" role="img" aria-label="Client portrait"><polygon points="59,0 118,32 118,96 59,128 0,96 0,32" fill="#e7ddd2"/></svg>
    <h5>Mara Lindqvist</h5><div class="role">Creative Director</div>
    <p>Lorem Ipsum simply dummy text printing and typesetting industry simply dummy a psum is simply dummy</p>
    <div class="stars">★★★★★</div>
  </div>
  <div class="testi" style="left:613px;top:3066px;">
    <svg class="abs" style="left:22px;top:50px;" width="118" height="128" viewBox="0 0 118 128" role="img" aria-label="Client portrait"><polygon points="59,0 118,32 118,96 59,128 0,96 0,32" fill="#c9ced6"/></svg>
    <h5>Dorian Pell</h5><div class="role">Director</div>
    <p>Lorem Ipsum simply dummy text printing and typesetting industry simply dummy a psum is simply dummy</p>
    <div class="stars">★★★★★</div>
  </div>
  <div class="dots" style="left:585px;top:3330px;gap:5px;"><i class="on" style="width:5px;height:5px"></i><i style="width:5px;height:5px;background:#555"></i><i style="width:5px;height:5px;background:#555"></i></div>
</section>

<!-- Contact -->
<section>
  <div class="footer">
    <div class="logo" style="left:110px;top:118px;"><span class="mark"></span><span class="name" style="color:var(--yellow);">Tall Fern Services</span></div>
    <div class="abs" style="left:114px;top:176px;font-weight:700;font-size:16px;color:var(--yellow);">DUCTLESS EXPERTS</div>
    <div class="foot-h" style="left:407px;">Quick Links</div>
    <div class="foot-list" style="left:410px;">› Home<br>› About us<br>› Our Services<br>› Gallery<br>› Blogs<br>› FAQ<br>› Contact us</div>
    <div class="foot-h" style="left:616px;">Contact information</div>
    <div class="foot-list" style="left:618px;line-height:26px;">
      <div>📍&nbsp;&nbsp;&nbsp;482 Quillon Avenue</div>
      <div style="padding-left:31px;">Harbin Falls, KY</div>
      <div style="padding-left:31px;">ZipCode : 12345</div>
      <div>☎&nbsp;&nbsp;&nbsp;&nbsp;(00) 123 456 7890</div>
      <div>✉&nbsp;&nbsp;&nbsp;&nbsp;info@tallfernservices.com</div>
    </div>
    <div class="foot-h" style="left:882px;">Follow us on social media</div>
    <div class="social"><i></i><i></i><i></i><i></i><i></i></div>
  </div>
  <div class="abs" style="left:192px;top:3395px;width:834px;height:336px;background:var(--yellow-soft);"></div>
  <div class="photo" role="img" aria-label="Smiling technician in a hard hat carrying toolboxes" style="left:70px;top:3332px;width:274px;height:399px;background:linear-gradient(180deg,#e3b11a 0%,#4f6b8c 40%,#2a3d58 100%);border-radius:120px 120px 10px 10px;"></div>
  <div class="abs" style="left:192px;top:3424px;width:834px;text-align:center;font-family:'Russo One',sans-serif;font-size:30px;color:var(--dark);">Contact Us Today</div>
  <div class="field" style="left:341px;top:3481px;width:194px;height:38px;">Name</div>
  <div class="field" style="left:546px;top:3481px;width:194px;height:38px;">Phone</div>
  <div class="field" style="left:752px;top:3481px;width:193px;height:38px;">Email</div>
  <div class="field" style="left:341px;top:3528px;width:604px;height:114px;">Message</div>
  <div class="btn btn-dark" style="left:532px;top:3667px;width:150px;height:32px;font-size:13px;">Send</div>
</section>

<!-- Bottom bar -->
<div class="bottom" style="left:113px;">Copyright © 2020 Tall Fern Services. All Right Reserved</div>
<div class="bottom" style="left:872px;">Privacy Policy &nbsp;&nbsp;|&nbsp;&nbsp; Terms &amp; Conditions</div>

</body>
</html>
```